Business card needed for the Rydo of Dry Cleaning!

We need a slick business card design for a new company based out of Montreal called Casiers Plimo&Zet inc. (in French) and Plimo&Zet Lockers inc. (in English). We're the Rydo of Laundry. We offer services of dry cleaning, laundry (wash&fold), minor clothing alterations, shoe repair and parcel delivery through 24/7 secured and connected lockers. Ordres are placed through our mobile application. Real time notification are sent to customers when their order is ready for pickup. The lockers will be placed throughout the downtown area, in condo and office towers, where a high density of busy people converge. It is simple, user-friendly, and most importantly convenient. We're the out of the box dry cleaner, literally.

Target Market(s)

1) Professional workers wearing suits daily
2) Campus students living in residences
3) People using laundromats
4) Families with children/yuppies who prefer to use their time doing something else than laundry

Industry/Entity Type

Dry Cleaning

Contact Information for Business Card

Name / Annick-Solène Trudel
Title / CEO & Founder
Company Name / Casiers Plimo&Zet inc. | Plimo&Zet Lockers inc.
Website www.plimozet.ca

Requirements
Must have
• Text Logo: Plimo&Zet - Nettoyeurs 24/7 Cleaners
• Logo on one side and contact info on the other (bilingual)
• Minimalist, pure design
• "We care" for your belongings feeling
• Professional, technological, clean & fresh look
Should not have
• No busy visuals. No rainbow colors.

```html
<!DOCTYPE html>
<html lang="en">
<head>
<meta charset="utf-8">
<title>Plimo&amp;Zet — Business Card</title>
<link rel="stylesheet" href="https://fonts.googleapis.com/css2?family=Open+Sans:wght@600;800&family=Marcellus&display=swap">
<style>
  :root {
    --page: #ffffff;
    --card-front: #ffffff;
    --card-back: #3259a6;
    --ink: #0d0d0d;
    --brand-blue: #3259a6;
    --on-blue: #ffffff;
    --edge: #2a2a2a;
    --shadow: rgba(0, 0, 0, 0.28);
  }
  * { box-sizing: border-box; margin: 0; padding: 0; }
  html, body {
    width: 933px;
    height: 1200px;
    overflow: hidden;
    background: var(--page);
  }
  .sheet {
    position: relative;
    width: 933px;
    height: 1200px;
  }
  .card {
    position: absolute;
    border-radius: 26px;
    box-shadow: 0 4px 14px var(--shadow);
  }
  .card--front {
    left: 50px;
    top: 50px;
    width: 826px;
    height: 530px;
    background: var(--card-front);
    border: 1px solid var(--edge);
    display: flex;
    align-items: center;
    justify-content: center;
  }
  .wordmark {
    display: flex;
    align-items: center;
    gap: 22px;
    margin-top: 0;
  }
  .wordmark__name {
    font-family: "Open Sans", sans-serif;
    font-weight: 800;
    font-size: 66px;
    letter-spacing: 6px;
    color: var(--ink);
    line-height: 1;
  }
  .wordmark__square {
    width: 58px;
    height: 58px;
    background: var(--brand-blue);
    border-radius: 8px;
  }
  .card--back {
    left: 50px;
    top: 610px;
    width: 832px;
    height: 535px;
    background: var(--card-back);
    color: var(--on-blue);
    text-align: center;
  }
  .back__mark {
    position: absolute;
    left: 378px;
    top: 132px;
    width: 120px;
    height: 116px;
    background: var(--on-blue);
    border-radius: 10px;
  }
  .contact {
    position: absolute;
    left: 0;
    right: 0;
    top: 264px;
  }
  .contact__name {
    font-family: "Open Sans", sans-serif;
    font-weight: 600;
    font-size: 21px;
    line-height: 1;
  }
  .contact__title {
    font-family: "Marcellus", serif;
    font-size: 16px;
    letter-spacing: 0.5px;
    margin-top: 12px;
    line-height: 1;
  }
  .contact__company {
    font-family: "Marcellus", serif;
    font-size: 17px;
    letter-spacing: 0.5px;
    margin-top: 18px;
    line-height: 1;
  }
  .contact__web {
    font-family: "Marcellus", serif;
    font-weight: 700;
    font-size: 16px;
    margin-top: 12px;
    line-height: 1;
  }
</style>
</head>
<body>
  <main class="sheet">
    <section class="card card--front" aria-label="Card front">
      <div class="wordmark">
        <span class="wordmark__name">PLIMO&amp;ZET</span>
        <span class="wordmark__square" aria-hidden="true"></span>
      </div>
    </section>

    <section class="card card--back" aria-label="Card back">
      <div class="back__mark" aria-hidden="true"></div>
      <div class="contact">
        <p class="contact__name">Annick-Solène Trudel</p>
        <p class="contact__title">CEO &amp; FOUNDER</p>
        <p class="contact__company">CASIERS PLIMO&amp;ZET INC. | PLIMO&amp;ZET LOCKERS INC</p>
        <p class="contact__web">www.plimozet.ca</p>
      </div>
    </section>
  </main>
</body>
</html>
```